Need a small Brochure Designing for a High Tech LED Spotlight

This is an expensive product and the best of it's kind in the world, so it needs to be marketed to intelligent, forward thinking people who appreciate and pay for excellent design and innovation. The type of people who buy Quince products i guess. It needs to be clean. The colours do not need to be in keep with our website, but our logo does need to be on the brochure. I have attached a dcoument with all the text, the order the text goes in and an idea of how i want the first page to look. All images and logos have been attached too.

Target Market(s)

This is aimed at people with high disposible incomes who spend money on the best designed products and the latest technology. The type of people who buy Quince products.

Industry/Entity Type

Product

Requirements
Must have
• The work needs to be editable by us using indesign

The pages need to be A5. I'm not sure how many pages the brochure needs to be as it does need to be clean and be spaced out well. On the file that contains the text i've indicated that 8 pages would be good.

The logos i attached - 1) Kelo Product Design Award, 2) Z Technology Award, 3) Blue Fern Design Award and 4) Keen Design Award all need to be at the bottom of the front page, quite small, but still able to see them well.

- Needs to have a QR code so that smart phones can scan the code and be taken to a pol vane clip - QR code is attached.
- Needs to have Plimbo Icon - @KestrowHomeCo
Nice to have
• Nice to remind customers on each page that the product has a 5 year Warranty and we have a 365 day Returns Policy.

```html
<!DOCTYPE html>
<html lang="en">
<head>
<meta charset="utf-8">
<title>K9 7w LED Spotlight – Brochure Spread</title>
<link href="https://fonts.googleapis.com/css2?family=PT+Sans:wght@400;700&display=swap" rel="stylesheet">
<style>
  :root {
    --backdrop: #e6e5e1;
    --green-dark: #6c8820;
    --green: #86a42b;
    --green-light: #a9c63c;
    --tab-light: #b6d046;
    --ink-white: #ffffff;
    --paper: #ffffff;
  }
  * { box-sizing: border-box; margin: 0; padding: 0; }
  html, body {
    width: 1200px; height: 803px; overflow: hidden;
    background: var(--backdrop);
    font-family: "PT Sans", sans-serif;
  }
  .spread {
    position: absolute; left: 110px; top: 40px;
    width: 980px; height: 723px;
    display: flex;
    box-shadow: 0 6px 24px rgba(0,0,0,.18);
  }
  .page {
    position: relative; width: 490px; height: 723px;
    background: var(--paper); overflow: hidden;
  }
  .page--left::after, .page--right::after {
    content: ""; position: absolute; top: 0; bottom: 0; width: 24px; pointer-events: none;
  }
  .page--left::after { right: 0; background: linear-gradient(to left, rgba(0,0,0,.16), transparent); }
  .page--right::after { left: 0; background: linear-gradient(to right, rgba(0,0,0,.16), transparent); }

  .photo { position: absolute; left: 0; right: 0; top: 0; height: 420px; }
  .photo--city {
    background:
      radial-gradient(ellipse 60% 30% at 55% 85%, rgba(226,170,80,.55), transparent 70%),
      linear-gradient(180deg, #1e2450 0%, #3b4a8a 40%, #5a6aa0 62%, #6b5a4e 82%, #1a1a22 100%);
  }
  .photo--interior {
    background:
      linear-gradient(180deg, #f4f4f2 0%, #e9e9e6 38%, #d9c4a6 55%, #c08d5e 75%, #a8703f 100%);
  }

  .web-tab {
    position: absolute; top: 14px; height: 30px;
    display: flex; align-items: center; padding: 0 22px;
    background: linear-gradient(90deg, var(--green), var(--tab-light));
    color: var(--ink-white); font-size: 8px; letter-spacing: .2px;
  }
  .page--left .web-tab { left: 0; width: 230px; border-radius: 0 0 18px 0; top: 0; height: 38px; padding-top: 8px; }
  .page--right .web-tab { right: 0; width: 230px; border-radius: 0 0 0 18px; top: 0; height: 38px; padding-top: 8px; justify-content: flex-end; }

  .panel {
    position: absolute; left: 0; right: 0; top: 420px; bottom: 0;
    background: linear-gradient(180deg, var(--green) 0%, var(--green-dark) 100%);
    color: var(--ink-white);
    padding: 18px 34px 0;
  }
  .rule {
    position: absolute; left: 34px; right: 34px; height: 0;
    border-top: 2px dotted rgba(255,255,255,.85);
  }
  .rule--top { top: 16px; }
  .rule--bottom { bottom: 36px; }
  .columns {
    position: absolute; left: 34px; right: 34px; top: 28px; bottom: 46px;
    display: grid; grid-template-columns: 1fr 1fr; column-gap: 18px;
  }
  .col p { font-size: 8.4px; line-height: 1.28; margin-bottom: 8px; }
  .col strong { font-weight: 700; }
  .pull-quote { font-weight: 700; }
  .section-title { font-size: 15px; font-weight: 700; margin: 2px 0 6px; line-height: 1.1; }
  .page-number {
    position: absolute; bottom: 28px; left: 50%; transform: translateX(-50%);
    width: 56px; height: 16px; border-radius: 8px;
    background: var(--paper); color: var(--green-dark);
    font-size: 10px; font-weight: 700; display: flex; align-items: center; justify-content: center;
  }
</style>
</head>
<body>
  <main class="spread">
    <section class="page page--left">
      <div class="photo photo--city" role="img" aria-label="Night skyline with a tall illuminated glass tower and lit apartment blocks along a waterfront"></div>
      <div class="web-tab">www.kestrowhome.co</div>
      <div class="panel">
        <div class="rule rule--top"></div>
        <div class="columns">
          <div class="col">
            <p>LEDs used to be prohibitively expensive, but advances in semiconductor technology mean they're now brighter and more affordable than before... it's easy to see why they're becoming so popular. <strong>Glowcheck?</strong></p>
            <p><strong>With its unrivalled performance and quality, the K9 7w is the most technologically advanced LED Spotlight in the world. Kestrow Home Co Managing Director Dara Voll talks about the K9 7w LED Spot:</strong></p>
            <p>"I've been working with the manufacturer of this exceptional product since their inception in 2008. They've received more than a hundred world patents and safety certifications so far – as far as I am concerned, there isn't an LED manufacturer in the world that comes close to their expertise and attention to detail.</p>
          </div>
          <div class="col">
            <p>"Since its creation, the company has won a number of prestigious international design awards, such as the Kelo Product Design Award, the Z Technology Award, the Blue Fern Design Award, and the Keen Design Award.</p>
            <p>"With high-quality, industry-leading performance, they've become the first choice for professional buyers and lighting designers in recent years. They're basically the Quince of the LED lighting industry – we're talking beautifully designed products that are miles ahead of the competition!</p>
            <p class="pull-quote">"The K9 Is The Ultimate In Lighting For The Discerning, Design Conscious And Forward Thinking Person"</p>
          </div>
        </div>
        <div class="rule rule--bottom"></div>
        <div class="page-number">4</div>
      </div>
    </section>

    <section class="page page--right">
      <div class="photo photo--interior" role="img" aria-label="Bright open-plan kitchen and living room with pendant lights, white island, bar stools and polished timber floor"></div>
      <div class="web-tab">www.kestrowhome.co</div>
      <div class="panel">
        <div class="rule rule--top"></div>
        <div class="columns">
          <div class="col">
            <h2 class="section-title">Heat Dissipation</h2>
            <p><strong>The brightness of all LEDs deteriorates over time. Just how quickly, though, is almost exclusively down to how well the lamp can dissipate heat.</strong></p>
            <p><strong>Heat is the biggest enemy of the LED. Without proper heat dissipation, the critical components of any LED lamp will fail or degrade quickly. So if the LED spotlight doesn't have a well-designed, thorough heat dissipation system, the quality of light will easily degrade to an unacceptable level, with the LED simply failing very quickly.</strong></p>
            <p><strong>The K9 7w is crafted from the finest raw materials and uses a cutting edge heat dissipation system similar to that used</strong></p>
          </div>
          <div class="col">
            <p><strong>to cool fuel tanks on Halvern Aerospace space shuttles and brake callipers on Velo Circuit cars.</strong></p>
            <p><strong>This beautiful, intuitive patented design has won multiple international awards</strong></p>
            <h2 class="section-title">Brightness</h2>
            <p>Mirrox manufacture the most advanced and powerful LED chips in the world. While rival companies now produce very reasonable alternatives, there's still no substitute for Mirrox.</p>
            <p>The K9 uses the very latest Mirrox QT-4 Chip, which produces 580 warm white lumens. With 83 lumens per watt, the K9 is considerably more powerful than a 50w halogen – and</p>
          </div>
        </div>
        <div class="rule rule--bottom"></div>
        <div class="page-number">5</div>
      </div>
    </section>
  </main>
</body>
</html>
```